Sports predictions portal

We need 8 html pages for portal who provides Matchday Forecasts. All website pages should match with our page schemes (in an attachment). It's only requirement. All other it's up to designer. We need nice looking, professional website design.
Thank you!

```html
<!DOCTYPE html>
<html lang="en">
<head>
<meta charset="utf-8">
<title>Matchday Forecasts</title>
<link rel="stylesheet" href="https://fonts.googleapis.com/css2?family=Roboto:wght@400;500;700&family=Open+Sans:wght@400;600;700&display=swap">
<style>
:root{
  --header-bg:#18181a;
  --header-bg2:#232325;
  --nav-top:#f7f7f7;
  --nav-bottom:#d6d6d6;
  --nav-line:#bdbdbd;
  --page-bg:#f4f4f4;
  --card-bg:#f7f7f7;
  --card-border:#dedede;
  --text:#222;
  --muted:#555;
  --red:#d7202a;
  --blue:#1a8fd6;
  --link:#1b7fcf;
  --slate:#4d5b69;
  --table-head:#2e2e2e;
  --footer-bg:#23232a;
  --footer-text:#8f8f96;
  --white:#fff;
}
*{box-sizing:border-box;margin:0;padding:0}
html,body{width:1200px;height:1181px;overflow:hidden}
body{font-family:"Open Sans",Arial,sans-serif;color:var(--text);background:var(--page-bg);position:relative}
.site-header{position:absolute;left:0;top:0;width:1200px;height:82px;background:linear-gradient(var(--header-bg2),var(--header-bg))}
.brand{position:absolute;left:162px;top:20px;color:var(--white);font-family:"Roboto",sans-serif;font-weight:700;font-size:25px}
.login-form{position:absolute;left:660px;top:19px;display:flex;gap:8px}
.field{width:142px}
.field .input{height:27px;background:#d9d9d9;border:1px solid #bcbcbc;border-radius:2px;font-size:12px;color:#888;padding:6px 8px}
.field a{display:block;color:var(--link);font-size:11px;margin-top:5px;text-decoration:none}
.login-btn{width:74px;height:27px;background:var(--red);color:var(--white);font-family:"Roboto",sans-serif;font-size:16px;text-align:center;line-height:27px;border-radius:2px;margin-left:4px}
.main-nav{position:absolute;left:0;top:82px;width:1200px;height:36px;background:linear-gradient(var(--nav-top),var(--nav-bottom));border-bottom:1px solid #c4c4c4;display:flex;padding-left:162px}
.main-nav a{display:flex;align-items:center;padding:0 20px;font-family:"Roboto",sans-serif;font-size:13px;font-weight:500;color:#222;text-decoration:none;border-right:1px solid var(--nav-line);height:36px}
.main-nav a.home{padding:0 20px 0 24px}
.slider{position:absolute;left:162px;top:139px;width:600px;height:307px;background:linear-gradient(160deg,#5c8fd0 0%,#a7c4e3 35%,#8a6a58 60%,#2c3e78 100%)}
.slide-caption{position:absolute;left:0;bottom:0;width:600px;height:78px;background:rgba(20,20,24,.82);padding:9px 12px;color:var(--white)}
.slide-meta{font-size:10px;display:flex;gap:18px;align-items:center}
.slide-meta span{display:flex;align-items:center;gap:6px}
.slide-title{font-family:"Roboto",sans-serif;font-size:16.5px;font-weight:500;margin-top:6px}
.slide-excerpt{font-size:11.5px;margin-top:6px}
.slide-excerpt a{color:var(--link);text-decoration:none}
.slide-arrows{position:absolute;right:8px;bottom:17px;display:flex;gap:9px}
.arrow{width:43px;height:43px;border-radius:50%;border:2px solid var(--white);display:flex;align-items:center;justify-content:center}
.arrow.dim{border-color:#8a8a8a}
.section-title{position:absolute;left:162px;top:464px;font-family:"Roboto",sans-serif;font-size:19px;font-weight:700}
.pred-box{position:absolute;left:162px;width:600px;background:var(--white);border:1px solid var(--card-border);border-radius:3px;overflow:hidden}
.pred-box.vip{top:497px}
.pred-box.free{top:736px}
.pred-box h3{height:37px;line-height:37px;text-align:center;color:var(--red);font-family:"Roboto",sans-serif;font-weight:500;font-size:15px;background:linear-gradient(#fafafa,#e2e2e2)}
table{width:100%;border-collapse:collapse;font-size:11px}
th{background:var(--table-head);color:var(--white);font-family:"Roboto",sans-serif;font-weight:500;font-size:11px;height:33px}
td{height:30.6px;border-top:1px solid #e4e4e4;border-right:1px solid #e4e4e4;text-align:center}
td:last-child{border-right:none}
td.tipster{text-align:left;padding-left:6px}
.plus{color:var(--blue);font-weight:700;font-size:15px;margin-left:3px}
.book{font-family:"Roboto",sans-serif;font-weight:700;font-size:12px;color:#111}
.ball{display:inline-block;width:17px;height:17px;border-radius:50%;background:radial-gradient(circle at 35% 35%,#fff,#e8e8e8 45%,#c42a2a 46%,#c42a2a 60%,#fff 61%);border:1px solid #bbb;vertical-align:middle}
.helmet{display:inline-block;width:18px;height:17px;border-radius:50% 50% 40% 40%;background:linear-gradient(135deg,#e0b020,#b33020);vertical-align:middle}
.side-card{position:absolute;left:780px;width:259px;background:var(--card-bg);border:1px solid var(--card-border)}
.reviews{top:139px;height:371px}
.card-head{position:relative;margin:7px 15px 0 -1px;height:29px;line-height:29px;padding-left:17px;color:var(--white);font-family:"Roboto",sans-serif;font-size:15px;font-weight:500}
.reviews .card-head{background:var(--red)}
.handicap .card-head{background:var(--slate);margin-right:15px}
.bonus-list{list-style:none;padding:0 12px 0 18px}
.bonus-list li{height:58px;border-bottom:1px solid #e2e2e2;position:relative;padding-top:8px}
.bonus-amount{font-size:12px}
.bonus-note{font-size:9.5px;color:var(--muted);margin-top:1px}
.stars{font-size:10px;letter-spacing:1px;margin-top:1px}
.bonus-brand{position:absolute;right:0;top:8px;font-family:"Roboto",sans-serif;font-weight:700;font-size:13px;color:#111}
.claim{position:absolute;right:0;top:28px;background:var(--blue);color:var(--white);font-size:9.5px;padding:3px 8px;border-radius:2px}
.view-more{display:inline-block;background:var(--blue);color:var(--white);font-size:9.5px;padding:4px 8px;border-radius:2px}
.reviews .view-more{margin:11px 0 0 18px}
.handicap{top:524px;height:322px}
.rank-list{list-style:none;padding:12px 12px 0 18px}
.rank-list li{height:31px;display:flex;align-items:center;font-size:12px}
.rank-num{width:16px;height:16px;border-radius:50%;background:var(--blue);color:var(--white);font-size:10px;text-align:center;line-height:16px;margin-right:10px}
.rank-name{flex:1;text-decoration:underline}
.rank-score{color:var(--link)}
.total-row{margin:0 0 0 18px;padding:4px 12px 6px 0;border-top:1px solid #ddd;border-bottom:1px solid #ddd;display:flex;justify-content:space-between;font-size:12px;font-weight:600}
.neg{color:var(--red);font-weight:600}
.profit{display:flex;justify-content:space-between;padding:6px 12px 0 18px;height:64px}
.profit-text{text-align:right;font-size:12px;font-weight:600}
.handicap .view-more{margin:4px 0 0 18px}
.site-footer{position:absolute;left:0;top:983px;width:1200px;height:198px;background:var(--footer-bg);color:var(--footer-text)}
.footer-brand{position:absolute;left:216px;top:18px;color:#c9c9cf;font-family:"Roboto",sans-serif;font-weight:700;font-size:19px}
.social{position:absolute;left:216px;top:81px;display:flex;gap:6px}
.social span{width:34px;height:34px;display:block}
.social .s1{background:#3b5998}.social .s2{background:#2aa4e0}.social .s3{background:#dc4a38}
.copyright{position:absolute;left:216px;top:146px;font-size:10.5px;line-height:15px;width:200px}
.divider{position:absolute;top:22px;width:1px;height:150px;background:#3a3a42}
.footer-col{position:absolute;top:20px}
.footer-col h4{color:var(--white);font-family:"Roboto",sans-serif;font-weight:500;font-size:12.5px;margin-bottom:9px}
.footer-col li{list-style:none;font-size:11px;line-height:19.4px}
</style>
</head>
<body>
<header class="site-header">
  <div class="brand">Matchday Forecasts</div>
  <div class="login-form">
    <div class="field"><div class="input">Login</div><a href="#">Registration</a></div>
    <div class="field"><div class="input">Password</div><a href="#">Forgot Password</a></div>
    <div class="login-btn">Login</div>
  </div>
</header>

<nav class="main-nav">
  <a class="home" href="#" aria-label="Home"><svg width="24" height="22" viewBox="0 0 24 22"><path d="M12 1 1 11h3v10h6v-6h4v6h6V11h3z" fill="#d7202a"/></svg></a>
  <a href="#">NEWS</a><a href="#">PREDICATIONS</a><a href="#">LEADERBOARDS</a><a href="#">BOOKMARKERS</a><a href="#">BONUSES</a>
</nav>

<section class="slider" role="img" aria-label="Photo of celebrating football fans lifting a trophy">
  <div class="slide-caption">
    <div class="slide-meta"><span>▦ June 11, 2014</span><span>▬ 0 Comment</span></div>
    <div class="slide-title">GLOBAL CUP 2014: GROUP G BETTING PREVIEW</div>
    <div class="slide-excerpt">Lorem Ipsum is simply dummy text of the printing and typesetting industry...<a href="#">[...]</a></div>
  </div>
  <div class="slide-arrows">
    <div class="arrow dim"><svg width="14" height="18"><path d="M10 2 3 9l7 7" stroke="#9a9a9a" stroke-width="2" fill="none"/></svg></div>
    <div class="arrow"><svg width="14" height="18"><path d="M4 2l7 7-7 7" stroke="#fff" stroke-width="2" fill="none"/></svg></div>
  </div>
</section>

<h2 class="section-title">PREDICATIONS</h2>

<section class="pred-box vip">
  <h3>VIP PREDICATIONS</h3>
  <table>
    <tr><th style="width:78px">TIPSTER</th><th style="width:80px">DATE &amp; TIME</th><th>EVENT</th><th style="width:64px">SPORT</th><th style="width:64px">ODD</th><th style="width:100px">BOOKMAKER</th></tr>
    <tr><td class="tipster">rovo71<span class="plus">+</span></td><td>00:30</td><td>Riverton - Porto Verde</td><td><span class="ball"></span></td><td>1.59</td><td class="book">Kingsfield</td></tr>
    <tr><td class="tipster">pelt9<span class="plus">+</span></td><td>18:00</td><td>Northfall (Fin) - Astron Kalos</td><td><span class="helmet"></span></td><td>3.28</td><td class="book">Kingsfield</td></tr>
    <tr><td class="tipster">GreyKestrel<span class="plus">+</span></td><td>19:00</td><td>Brezina (Cze) - Stari Most</td><td><span class="ball"></span></td><td>4.80</td><td class="book">Betnova</td></tr>
    <tr><td class="tipster">luck<span class="plus">+</span></td><td>19:00</td><td>Fjellvik (Nor) - Harbour Rovers</td><td><span class="helmet"></span></td><td>5.07</td><td class="book">Kingsfield</td></tr>
    <tr><td class="tipster">Halvard<span class="plus">+</span></td><td>20:45</td><td>Ardmore (Irl) - Adria Solin (cro)</td><td><span class="ball"></span></td><td>3.26</td><td class="book">Kingsfield</td></tr>
  </table>
</section>

<section class="pred-box free">
  <h3>FREE PREDICATIONS</h3>
  <table>
    <tr><th style="width:78px">TIPSTER</th><th style="width:80px">DATE &amp; TIME</th><th>EVENT</th><th style="width:64px">SPORT</th><th style="width:64px">ODD</th><th style="width:100px">BOOKMAKER</th></tr>
    <tr><td class="tipster">rovo71<span class="plus">+</span></td><td>00:30</td><td>Riverton - Porto Verde</td><td><span class="ball"></span></td><td>1.59</td><td class="book">Kingsfield</td></tr>
    <tr><td class="tipster">pelt9<span class="plus">+</span></td><td>18:00</td><td>Northfall (Fin) - Astron Kalos</td><td><span class="helmet"></span></td><td>3.28</td><td class="book">Kingsfield</td></tr>
    <tr><td class="tipster">GreyKestrel<span class="plus">+</span></td><td>19:00</td><td>Brezina (Cze) - Stari Most</td><td><span class="ball"></span></td><td>4.80</td><td class="book">Betnova</td></tr>
    <tr><td class="tipster">luck<span class="plus">+</span></td><td>19:00</td><td>Fjellvik (Nor) - Harbour Rovers</td><td><span class="helmet"></span></td><td>5.07</td><td class="book">Kingsfield</td></tr>
    <tr><td class="tipster">Halvard<span class="plus">+</span></td><td>20:45</td><td>Ardmore (Irl) - Adria Solin (cro)</td><td><span class="ball"></span></td><td>3.26</td><td class="book">Kingsfield</td></tr>
  </table>
</section>

<aside class="side-card reviews">
  <div class="card-head">BOOKMAKERS REVIEWS</div>
  <ul class="bonus-list">
    <li><div class="bonus-amount">100% UP TO $100</div><div class="bonus-note">First Deposit Bonus</div><div class="stars">★★★★★</div><span class="bonus-brand">Betnova</span><span class="claim">CLAIM</span></li>
    <li><div class="bonus-amount">100% UP TO $100</div><div class="bonus-note">First Deposit Bonus</div><div class="stars">★★★★★</div><span class="bonus-brand">Stakora</span><span class="claim">CLAIM</span></li>
    <li><div class="bonus-amount">100% UP TO $100</div><div class="bonus-note">First Deposit Bonus</div><div class="stars">★★★★★</div><span class="bonus-brand">Wagerline</span><span class="claim">CLAIM</span></li>
    <li><div class="bonus-amount">100% UP TO $100</div><div class="bonus-note">First Deposit Bonus</div><div class="stars">★★★★★</div><span class="bonus-brand">Kingsfield</span><span class="claim">CLAIM</span></li>
    <li><div class="bonus-amount">100% UP TO $100</div><div class="bonus-note">First Deposit Bonus</div><div class="stars">★★★★★</div><span class="bonus-brand">Oddsway</span><span class="claim">CLAIM</span></li>
  </ul>
  <span class="view-more">VIEW MORE ▸</span>
</aside>

<aside class="side-card handicap">
  <div class="card-head">WEEK TOP 5 HANDICAPPERS</div>
  <ol class="rank-list">
    <li><span class="rank-num">1</span><span class="rank-name">mira0042</span><span class="rank-score">+31.28</span></li>
    <li><span class="rank-num">2</span><span class="rank-name">Vantor</span><span class="rank-score">+29.54</span></li>
    <li><span class="rank-num">3</span><span class="rank-name">Tippfalke</span><span class="rank-score">+26.7</span></li>
    <li><span class="rank-num">4</span><span class="rank-name">Steelmint</span><span class="rank-score">+20.79</span></li>
    <li><span class="rank-num">5</span><span class="rank-name">Oren</span><span class="rank-score">+13</span></li>
  </ol>
  <div class="total-row"><span>July Total</span><span class="neg">-185.10</span></div>
  <div class="profit">
    <svg width="74" height="52" viewBox="0 0 74 52" aria-label="Profit bar chart">
      <rect x="0" y="14" width="10" height="38" fill="#2b5f9e"/>
      <rect x="12" y="0" width="10" height="52" fill="#d2492b"/>
      <rect x="24" y="8" width="10" height="44" fill="#f0a030"/>
      <rect x="36" y="20" width="10" height="32" fill="#7a6aa8"/>
      <rect x="48" y="32" width="10" height="20" fill="#2a9a9a"/>
      <rect x="60" y="26" width="10" height="26" fill="#8ab830"/>
    </svg>
    <div class="profit-text">Overall Profit<br><span class="neg">-206.10</span></div>
  </div>
  <span class="view-more">VIEW MORE ▸</span>
</aside>

<footer class="site-footer">
  <div class="footer-brand">Matchday Forecasts</div>
  <div class="social"><span class="s1"></span><span class="s2"></span><span class="s3"></span></div>
  <p class="copyright">Copyright © 2014 Matchday Forecasts. All Rights Reserved.</p>
  <div class="divider" style="left:450px"></div>
  <div class="divider" style="left:750px"></div>
  <div class="footer-col" style="left:541px">
    <h4>PARTNERS</h4>
    <ul><li>Lorem Ipsum is dummy</li><li>Lorem Ipsum is dummy</li><li>Lorem Ipsum is dummy</li><li>Lorem Ipsum is dummy</li><li>Lorem Ipsum is dummy</li><li>Lorem Ipsum is dummy</li></ul>
  </div>
  <div class="footer-col" style="left:859px">
    <h4>BOOKMAKER</h4>
    <ul><li>Punthaus</li><li>Betnova</li><li>Fairstake</li><li>Tallybet</li><li>Oddsway</li><li>Goalpost Bet</li><li>Kingsfield</li></ul>
  </div>
</footer>
</body>
</html>
```